Business Card Design for Varnor Facility Services

We are looking for a Business Card Design for the Company "Varnor Facility Services."
Front side:
- Company Logo (small)
- Company Name, address, pohone, website and personal data.
- white background, for text e.g. company colors (blue or green like in the logo)
Please use following data:
Company data:
Varnor Facility Services Kuttelbrand
Lindauweg 14
6391 Seewilen
www.varnor-fs.example
Person data:
Tobias Kuttelbrand
Geschäftsführer
+41 76 915 47 18
info@varnor-fs.example
Back side:
could be colored in blue or green
please use a big logo sing and some smaller icons to say what is all beeing offered in facility services, like cleaning, maintenance cleaning
industrial cleaning, caretaking, gardening, disposal. There is no need for everyone of the icons if there are similar or an icon is standing for more of them.
Cleaning Service
colors to use:
blue: HEX 246BB0
green: HEX 52B33E

```html
<!DOCTYPE html>
<html lang="de">
<head>
<meta charset="utf-8">
<title>Varnor Facility Services – Visitenkarte</title>
<link rel="stylesheet" href="https://fonts.googleapis.com/css2?family=Montserrat:wght@500;700&family=Open+Sans:ital,wght@0,700;1,400;1,600&display=swap">
<style>
  :root {
    --blue: #246bb0;
    --blue-card: #3070b0;
    --green: #52b33e;
    --photo-a: #eef1ee;
    --photo-b: #d9e6ea;
    --ink-soft: #e6e9ec;
    --page: #ffffff;
  }
  * { margin: 0; padding: 0; box-sizing: border-box; }
  html, body { width: 1200px; height: 1200px; overflow: hidden; background: var(--page); }
  body { position: relative; font-family: 'Montserrat', sans-serif; }

  .card {
    position: absolute; left: 241px; width: 726px; height: 414px;
    overflow: hidden; background: #fff;
  }
  .card--back { top: 129px; }
  .card--front { top: 663px; border: 1px solid var(--ink-soft); }

  .accent-bars { position: absolute; left: 43px; top: 0; display: flex; }
  .accent-bars span { width: 25px; height: 53px; }
  .accent-bars .g { background: var(--green); }
  .accent-bars .b { background: var(--blue-card); }

  .photo-fill {
    position: absolute; inset: 0;
    background: linear-gradient(110deg, var(--photo-a) 0%, #f2eee6 45%, var(--photo-b) 100%);
  }

  .brand {
    position: absolute; display: flex; align-items: center; gap: 10px;
    font-family: 'Montserrat', sans-serif; font-weight: 700;
    color: var(--blue-card); letter-spacing: 0.04em; white-space: nowrap;
  }
  .brand .mark { background: var(--green); flex: none; }
  .brand--large { left: 0; right: 0; top: 178px; justify-content: center; font-size: 34px; }
  .brand--large .mark { width: 22px; height: 22px; }
  .brand--small { right: 38px; top: 100px; font-size: 17px; }
  .brand--small .mark { width: 12px; height: 12px; }

  .wave { position: absolute; left: 0; bottom: 0; width: 726px; height: 140px; }

  .services {
    position: absolute; left: 0; right: 0; top: 340px; text-align: center;
    font-family: 'Open Sans', sans-serif; color: #fff;
  }
  .services h2 { font-weight: 700; font-size: 21px; letter-spacing: 0.01em; }
  .services p { font-style: italic; font-weight: 400; font-size: 15px; margin-top: 4px; }

  .person { position: absolute; left: 42px; top: 186px; }
  .person h1 { font-weight: 700; font-size: 29px; color: var(--blue-card); letter-spacing: 0.01em; }
  .person .role { font-weight: 500; font-size: 17px; color: var(--green); letter-spacing: 0.1em; margin-top: 2px; }

  .divider { position: absolute; left: 42px; right: 38px; top: 251px; height: 1px; background: var(--ink-soft); }

  .contact { position: absolute; left: 42px; top: 270px; list-style: none; }
  .contact li {
    display: flex; align-items: flex-start; gap: 13px;
    font-weight: 500; font-size: 14px; letter-spacing: 0.1em; line-height: 18px;
    color: var(--blue); margin-bottom: 11px;
  }
  .contact svg { width: 18px; height: 18px; flex: none; fill: var(--blue); }

  .footer { position: absolute; left: 0; bottom: 0; width: 726px; height: 40px; }
  .web {
    position: absolute; right: 30px; bottom: 14px;
    font-family: 'Open Sans', sans-serif; font-style: italic; font-weight: 600;
    font-size: 14px; color: #fff; white-space: nowrap;
  }
</style>
</head>
<body>

  <section class="card card--back" aria-label="Rückseite">
    <div class="photo-fill" role="img" aria-label="Hell überblendetes Foto von Reinigungskräften bei der Arbeit"></div>
    <div class="accent-bars"><span class="g"></span><span class="b"></span></div>

    <div class="brand brand--large"><span class="mark"></span>Varnor Facility Services</div>

    <svg class="wave" viewBox="0 0 726 140" preserveAspectRatio="none" aria-hidden="true">
      <path d="M300 35 C420 40 520 48 640 40 L726 20 L726 60 C600 80 470 60 300 35 Z" fill="var(--green)"/>
      <path d="M0 30 C90 5 200 0 300 20 C430 45 560 70 726 55 L726 140 L0 140 Z" fill="var(--blue-card)"/>
    </svg>

    <div class="services">
      <h2>SERVICES</h2>
      <p>Cleaning, Maintenance Cleaning, Industrial Cleaning, Caretaking, Gardening, Disposal</p>
    </div>
  </section>

  <section class="card card--front" aria-label="Vorderseite">
    <div class="accent-bars"><span class="g"></span><span class="b"></span></div>

    <div class="brand brand--small"><span class="mark"></span>Varnor Facility Services</div>

    <div class="person">
      <h1>TOBIAS KUTTELBRAND</h1>
      <p class="role">Geschäftsführer</p>
    </div>
    <div class="divider"></div>

    <ul class="contact">
      <li>
        <svg viewBox="0 0 24 24" aria-hidden="true"><path d="M12 2a7 7 0 0 0-7 7c0 5 7 13 7 13s7-8 7-13a7 7 0 0 0-7-7zm0 9.5A2.5 2.5 0 1 1 12 6.5a2.5 2.5 0 0 1 0 5z"/></svg>
        <span>Varnor Facility Services Kuttelbrand<br>Lindauweg 14 6391 Seewilen</span>
      </li>
      <li>
        <svg viewBox="0 0 24 24" aria-hidden="true"><path d="M2 9l10-6 10 6v11H2z M3 10l9 6 9-6" stroke="#fff" stroke-width="1.5"/></svg>
        <span>info@varnor-fs.example</span>
      </li>
      <li>
        <svg viewBox="0 0 24 24" aria-hidden="true"><path d="M6.6 10.8a15 15 0 0 0 6.6 6.6l2.2-2.2a1 1 0 0 1 1-.25 11.4 11.4 0 0 0 3.6.57 1 1 0 0 1 1 1V20a1 1 0 0 1-1 1A17 17 0 0 1 3 4a1 1 0 0 1 1-1h3.5a1 1 0 0 1 1 1c0 1.25.2 2.45.57 3.57a1 1 0 0 1-.25 1z"/></svg>
        <span>+41 76 915 47 18</span>
      </li>
    </ul>

    <svg class="footer" viewBox="0 0 726 40" aria-hidden="true">
      <polygon points="0,23 480,23 466,40 0,40" fill="var(--green)"/>
      <polygon points="510,0 726,0 726,40 478,40" fill="var(--blue-card)"/>
    </svg>
    <span class="web">www.varnor-fs.example</span>
  </section>

</body>
</html>
```